Maple Crest Venture Fund

Take current power point presentation and make it uniform in color and font, and create designs that pop throughout the presentation. Right now, it is dull and mundane.

```html
<!DOCTYPE html>
<html lang="en">
<head>
<meta charset="utf-8">
<title>Maple Crest Venture Fund – Presentation</title>
<link href="https://fonts.googleapis.com/css2?family=Poppins:wght@400;500;600;700&display=swap" rel="stylesheet">
<style>
:root{
  --blue:#1570c6;
  --blue-deep:#0f5fb0;
  --blue-light:#2d8be0;
  --ink:#3d3d3d;
  --muted:#6a6a6a;
  --grey:#6b6b6b;
  --page:#d9dadc;
  --white:#ffffff;
}
*{margin:0;padding:0;box-sizing:border-box}
html,body{width:1200px;height:763px;overflow:hidden}
body{background:var(--page);font-family:'Poppins',sans-serif;color:var(--ink);position:relative}
.slide{position:absolute;width:353px;height:199px;background:var(--white);box-shadow:2px 3px 8px rgba(0,0,0,.25);overflow:hidden}
.abs{position:absolute}
.title{position:absolute;left:12px;top:11px;font-weight:700;color:var(--blue);font-size:11.5px;letter-spacing:.1px;padding-left:6px;border-left:4px solid var(--blue);line-height:12px}
.foot-logo{position:absolute;left:13px;top:179px;font-weight:700;font-size:11px;color:var(--blue);letter-spacing:.2px}
.foot-line{position:absolute;left:44px;right:12px;top:189px;height:0;border-top:.6px solid #777}
.foot-num{position:absolute;right:8px;top:186px;font-size:3.5px;color:#555}
.center{text-align:center}
.h-blue{color:var(--blue);font-weight:700}

/* cover */
.cover{background:var(--blue)}
.cover-bg{position:absolute;inset:0;background:linear-gradient(120deg,#1467bf 0%,#1b7bd4 45%,#1266bb 100%)}
.cover-name{position:absolute;left:0;right:0;top:52px;text-align:center;color:#fff;font-weight:700;font-size:48px;letter-spacing:2px;line-height:54px}
.cover-sub{position:absolute;left:0;right:0;top:108px;text-align:center;color:#fff;font-size:7.5px;letter-spacing:.8px}
.cover-tag{position:absolute;left:0;right:0;top:136px;text-align:center;color:#fff;font-weight:500;font-size:10.5px;letter-spacing:.8px}
.cover-rule{position:absolute;left:0;right:0;top:173px;border-top:.7px solid rgba(255,255,255,.8)}
.cover-web{position:absolute;left:50%;transform:translateX(-50%);top:168px;background:#1670c8;color:#fff;font-size:6px;letter-spacing:2.5px;padding:0 4px}
.dots{position:absolute;right:10px;top:10px;display:grid;grid-template-columns:repeat(4,5px);gap:3px}
.dots i{width:1.4px;height:1.4px;background:#fff;border-radius:50%;display:block}

/* disclosure */
.disc-box{position:absolute;left:29px;top:30px;width:296px;height:136px;border:1px solid #999;border-radius:9px;padding:14px 6px 4px}
.disc-box p{font-size:3.6px;line-height:5.6px;color:#555;margin-bottom:5px;text-align:justify}
.disc-pill{position:absolute;left:50%;transform:translateX(-50%);top:-6px;background:var(--blue);color:#fff;font-weight:700;font-size:8px;padding:1px 4px;border-radius:2px;outline:2px solid #fff}

/* agenda */
.agenda{position:absolute;font-size:6px;color:var(--blue);font-weight:500;line-height:12px}
.agenda li{list-style:none;position:relative;padding-left:9px}
.agenda li::before{content:"";position:absolute;left:0;top:3.5px;width:3.6px;height:3.6px;border:.8px solid var(--blue)}
.agenda ul.sub{margin:-2px 0 0 10px}
.agenda ul.sub li{font-size:4.6px;color:#555;font-weight:400;line-height:8.2px;padding-left:10px}
.agenda ul.sub li::before{width:1.6px;height:1.6px;background:#555;border:0;top:3.3px;left:2px}

/* objectives */
.goal-bracket{position:absolute;left:35px;top:46px;width:58px;height:52px;border-left:.8px solid var(--blue);border-top:.8px solid var(--blue);border-bottom:.8px solid var(--blue);border-right:0}
.check{position:absolute;width:5px;height:5px;border:.6px solid #666}
.check::after{content:"";position:absolute;left:1px;top:-1px;width:2px;height:4px;border-right:.8px solid var(--blue);border-bottom:.8px solid var(--blue);transform:rotate(40deg)}
.obj-item{position:absolute;left:108px;font-size:4.2px;line-height:5.3px;color:#555;width:210px}

/* strategy */
.strat-col{position:absolute;top:104px;width:74px;text-align:center}
.strat-icon{width:16px;height:16px;background:var(--blue);margin:0 auto 7px;display:flex;align-items:center;justify-content:center}
.strat-col b{display:block;color:var(--blue);font-size:5px;font-weight:600}
.strat-col span{font-size:4.2px;color:#666;line-height:5.4px;display:block}

/* section slide */
.sec-name{position:absolute;left:0;right:0;top:48px;text-align:center;font-weight:700;font-size:48px;letter-spacing:2px;color:var(--blue);line-height:54px}
.sec-sub{position:absolute;left:0;right:0;top:97px;text-align:center;font-size:6.5px;letter-spacing:.6px;color:#444}
.sec-band{position:absolute;left:44px;width:267px;top:120px;height:36px;background:var(--blue);color:#fff;text-align:center;padding-top:3px}
.sec-band b{font-size:7px;display:block}
.sec-band span{font-size:6px;line-height:8px;display:block;width:150px;margin:0 auto}

/* org chart */
.node{position:absolute;background:var(--blue);color:#fff;font-weight:600;text-align:center;border-radius:10px;font-size:3.5px;box-shadow:1px 2px 3px rgba(0,0,0,.25)}
.node small{display:block;font-size:2.4px;font-weight:400}
.photo{position:absolute;width:24px;height:24px;border-radius:50%;border:1.5px solid var(--blue);background:linear-gradient(#8d8d8d,#4a4a4a)}
.hex{position:absolute;width:26px;height:26px;border-radius:50%;border:1.5px solid var(--blue);background:#fff;display:flex;align-items:center;justify-content:center;font-weight:700;color:var(--blue);font-size:7px}

/* bios */
.bio{position:absolute;top:52px;text-align:center}
.bio b{display:block;color:var(--blue);font-size:7px;font-weight:700}
.bio small{display:block;color:var(--blue);font-size:3.6px;margin-bottom:4px}
.bio p{font-size:3.4px;line-height:4.5px;color:#666;text-align:justify}

/* contact */
.contact-h{position:absolute;left:0;right:0;top:62px;text-align:center;font-weight:700;font-size:15.5px;color:#333;letter-spacing:.3px}
.contact-h em{font-style:normal;color:var(--blue)}
.contact-p{position:absolute;left:45px;right:45px;top:83px;text-align:center;font-size:4.4px;line-height:6px;color:#555}
.contact-band{position:absolute;left:33px;width:287px;top:105px;height:43px;background:var(--blue);color:#fff;font-size:5.4px;line-height:7px}
.contact-item{position:absolute;top:15px;display:flex;align-items:center;gap:5px}
.contact-web{position:absolute;left:0;right:0;top:155px;text-align:center;font-size:6.5px;letter-spacing:2.6px;color:#333}
.contact-web b{color:var(--blue);font-weight:600}
</style>
</head>
<body>

<!-- Slide 1 : cover -->
<section class="slide cover" style="left:52px;top:61px">
  <div class="cover-bg" role="img" aria-label="Faded stock market figures and rising arrow chart in blue tones"></div>
  <div class="dots"><i></i><i></i><i></i><i></i><i></i><i></i><i></i><i></i><i></i><i></i><i></i><i></i></div>
  <div class="cover-name">MCVF</div>
  <div class="cover-sub">Maple Crest Venture Fund</div>
  <div class="cover-tag">BUSINESS Presentation Template</div>
  <div class="cover-rule"></div>
  <div class="cover-web">www.<b>maplecrestfund</b>.com</div>
</section>

<!-- Slide 2 : disclosure -->
<section class="slide" style="left:425px;top:61px">
  <div class="disc-box">
    <div class="disc-pill">DISCLOSURE</div>
    <p>This Presentation is a summary only and does not constitute an offer to sell or a solicitation of any offer to buy any securities. Any such offer will be made solely to qualified investors by means of an offering memorandum and related subscription materials.</p>
    <p>No assurance can be given that the objectives discussed herein will be achieved, and results may vary on a quarterly or annual basis. Past performance is not indicative of future results.</p>
    <p>Prospective reviewers should not construe this Presentation as legal, accounting, tax or investment advice, and each reviewer should consult its own counsel and advisors as to all related matters.</p>
    <p>Certain information herein has been provided by third parties and has not been independently verified by MCVF. MCVF makes no warranty as to the accuracy or completeness of such information and accepts no liability for losses arising from its use.</p>
    <p>This Presentation is confidential and proprietary to MCVF and is not to be disclosed, in whole or in part, to any party other than the person to whom it has been delivered and that person's professional advisors.</p>
  </div>
  <div class="foot-logo">MCVF</div><div class="foot-line"></div><div class="foot-num">2</div>
</section>

<!-- Slide 3 : agenda -->
<section class="slide" style="left:796px;top:61px">
  <div class="title">AGENDA</div>
  <ul class="agenda" style="left:44px;top:64px">
    <li>Objectives</li>
    <li>Strategy</li>
    <li>The MCVF organization
      <ul class="sub"><li>Senior Management</li><li>MCVF's competitive advantage</li><li>How we are different</li></ul>
    </li>
    <li>Performance</li>
    <li>Structure &amp; Terms</li>
  </ul>
  <ul class="agenda" style="left:165px;top:64px">
    <li>Why Direct Investments?
      <ul class="sub" style="line-height:10px">
        <li style="line-height:9.6px">Why MCVF' Direct Invest Strategy?</li>
        <li style="line-height:9.6px">Industry Overview</li>
        <li style="line-height:10.6px">Differentiation Between PIPEs and Direct Investments</li>
        <li style="line-height:10.6px">Capital/Deal Structure</li>
        <li style="line-height:10.6px">Process</li>
        <li style="line-height:10.6px">Protection/Risk</li>
      </ul>
    </li>
  </ul>
  <div class="foot-logo">MCVF</div><div class="foot-line"></div><div class="foot-num">3</div>
</section>

<!-- Slide 4 : objectives -->
<section class="slide" style="left:52px;top:281px">
  <div class="title">OBJECTIVES</div>
  <div class="goal-bracket"></div>
  <div class="abs h-blue" style="left:46px;top:42px;font-size:11px;font-weight:600;line-height:11.5px;background:#fff;padding-right:2px">Investment<br>Goal</div>
  <div class="check" style="left:51px;top:72px"></div>
  <div class="abs" style="left:61px;top:70px;font-size:4.4px;line-height:5.5px;color:#555">Superior risk-adjusted returns while<br>preserving capital in all market environments.</div>
  <svg class="abs" style="left:92px;top:95px" width="6" height="6" viewBox="0 0 6 6"><path d="M1 0.5 L4 3 L1 5.5" fill="none" stroke="#1570c6" stroke-width="1.2"/></svg>
  <div class="abs h-blue" style="left:99px;top:94px;font-size:5.5px;font-weight:600">Our Approach to Meeting Objectives</div>
  <div class="check" style="left:101px;top:107px"></div><div class="obj-item" style="top:107px">Strategically negotiate private investments in publicly traded companies.</div>
  <div class="check" style="left:101px;top:117px"></div><div class="obj-item" style="top:117px">Offer alternative capital solutions for small and micro-cap public companies with market capitalizations up to $2 billion.</div>
  <div class="check" style="left:101px;top:133px"></div><div class="obj-item" style="top:133px">Employ a specialized strategy for collateralized investments.</div>
  <div class="check" style="left:101px;top:143px"></div><div class="obj-item" style="top:143px">Maintain a well-diversified portfolio through tranching and sub-tranching of investments and milestones.</div>
  <div class="check" style="left:101px;top:159px"></div><div class="obj-item" style="top:159px">Execute investments over a 1- to 4-year horizon, ensuring liquidity opportunities throughout.</div>
  <div class="foot-logo">MCVF</div><div class="foot-line"></div><div class="foot-num">4</div>
</section>

<!-- Slide 5 : investment strategy -->
<section class="slide" style="left:425px;top:281px">
  <div class="title">INVESTMENT STRATEGY</div>
  <div class="abs center h-blue" style="left:0;right:0;top:40px;font-size:6.2px">MCVF FUNDING SPECIALIZATION</div>
  <div class="abs center" style="left:38px;right:38px;top:51px;font-size:4.3px;line-height:5.6px;color:#555">MCVF focuses on financing Development Stage, Emerging Growth, and Distressed public companies. This is achieved through a structured approach, wherein investments are tranched over a one- to four-year timeframe.</div>
  <div class="abs center h-blue" style="left:0;right:0;top:72px;font-size:6.2px">OBJECTIVES:</div>
  <div class="abs center" style="left:0;right:0;top:81px;font-size:5px;color:#555">Our strategy serves three key purposes:</div>
  <div class="strat-col" style="left:36px">
    <div class="strat-icon"><svg width="10" height="10" viewBox="0 0 10 10"><circle cx="5" cy="4" r="2.6" fill="none" stroke="#fff" stroke-width=".8"/><path d="M4 7h2M4 8.5h2" stroke="#fff" stroke-width=".8"/></svg></div>
    <b>Minimize Dilution:</b><span>Limits the dilution of the issuer's common stock.</span>
  </div>
  <div class="strat-col" style="left:140px">
    <div class="strat-icon"><svg width="10" height="10" viewBox="0 0 10 10"><path d="M2 8V6M4 8V4.5M6 8V5.5M8 8V2.5" stroke="#fff" stroke-width="1"/><path d="M1 8.6h8" stroke="#fff" stroke-width=".6"/></svg></div>
    <b>Mitigate Risk:</b><span>Reduces exposure by allowing cessation of further investment in the event of a material adverse change.</span>
  </div>
  <div class="strat-col" style="left:244px">
    <div class="strat-icon"><svg width="10" height="10" viewBox="0 0 10 10"><path d="M3 3h4l1.5 5h-7z" fill="none" stroke="#fff" stroke-width=".8"/><path d="M4 3L3.5 1.5h3L6 3" fill="none" stroke="#fff" stroke-width=".8"/></svg></div>
    <b>Protect Capital:</b><span>Safeguards against losses stemming from fraud or corporate malfeasance.</span>
  </div>
  <div class="foot-logo">MCVF</div><div class="foot-line"></div><div class="foot-num">5</div>
</section>

<!-- Slide 6 : section -->
<section class="slide" style="left:796px;top:281px">
  <div class="sec-name">MCVF</div>
  <div class="sec-sub">Maple Crest Venture Fund</div>
  <div class="sec-band"><b>THE ORGANIZATION</b><span>MCVF's Competitive Advantage: What Sets Us Apart</span></div>
  <div class="foot-logo">MCVF</div><div class="foot-line"></div><div class="foot-num">6</div>
</section>

<!-- Slide 7 : org chart -->
<section class="slide" style="left:52px;top:503px">
  <div class="title">THE MCVF ORGANIZATION</div>
  <div class="abs center h-blue" style="left:0;right:0;top:40px;font-size:6.2px">MCVF'S COMPETITIVE ADVANTAGE</div>
  <div class="abs center" style="left:26px;right:26px;top:50px;font-size:4.3px;line-height:6.2px;color:#555">MCVF is industry-agnostic, with a focus on identifying <b style="color:#222">"super value"</b> companies that possess strong operating entities and capable management teams. Our flexible organizational structure allows us to tailor each investment to address specific challenges—or a series of challenges—faced by these typically undervalued issuers.</div>
  <svg class="abs" style="left:0;top:0" width="353" height="199"><path d="M176 112V139M114 139H240" stroke="#bbb" stroke-width=".6" fill="none"/></svg>
  <div class="hex" style="left:163px;top:76px">MCVF</div>
  <div class="node" style="left:153px;top:97px;width:46px;height:11px;line-height:11px">Crestline Holdings, LLC</div>
  <div class="photo" style="left:102px;top:127px" role="img" aria-label="Portrait photo of Daniel Ashworth"></div>
  <div class="node" style="left:90px;top:147px;width:46px;height:17px;padding-top:4px">DANIEL ASHWORTH<small>MEMBER</small></div>
  <div class="photo" style="left:164px;top:127px" role="img" aria-label="Portrait photo of Rohan Mehra"></div>
  <div class="node" style="left:152px;top:147px;width:46px;height:17px;padding-top:4px">ROHAN MEHRA<small>MEMBER</small></div>
  <div class="photo" style="left:228px;top:127px" role="img" aria-label="Portrait photo of Peter Lindqvist"></div>
  <div class="node" style="left:216px;top:147px;width:46px;height:17px;padding-top:4px">PETER LINDQVIST<small>MEMBER</small></div>
  <div class="foot-logo">MCVF</div><div class="foot-line"></div><div class="foot-num">7</div>
</section>

<!-- Slide 8 : bios -->
<section class="slide" style="left:425px;top:503px">
  <div class="title">THE MCVF ORGANIZATION</div>
  <div class="bio" style="left:21px;width:66px"><b>DANIEL ASHWORTH</b><small>MEMBER</small>
    <p>Daniel Ashworth is a Founder and Member of Crestline Holdings, bringing over 17 years of experience in private investment in public equity transactions. Before launching his own funds, he co-founded multiple investment funds and managed portfolios for a boutique family of funds. He began his career as an analyst for a large hedge fund, overseeing fifty-five portfolio companies. He holds a Bachelor of Arts in Finance.</p>
  </div>
  <div class="bio" style="left:114px;width:70px"><b>ROHAN MEHRA</b><small>MEMBER</small>
    <p>Rohan Mehra is a Founder and Member of Crestline Holdings with extensive experience investing in publicly traded companies since 2011. He also co-founded several investment funds. His professional background spans roles at a state agency, a class action administration firm and an IT company prior to his move into finance. He earned a law degree and a Bachelor's degree in Philosophy, Politics and Law.</p>
  </div>
  <div class="bio" style="left:209px;width:125px"><b>PETER LINDQVIST</b><small>MEMBER</small>
    <p>Peter Lindqvist is a business executive with extensive C-level and board leadership experience across private and public companies. He is currently a Founder and Member of Crestline Holdings. Previously he served as Founder, Chairman and Chief Executive Officer of a company specializing in harvesting and storing stem cells in the U.S. and abroad, and later as CEO and Chairman of a related firm.</p>
    <p style="margin-top:4px">Before joining MCVF, he worked as a licensed investment banker providing microcap advisory and capital introduction services to publicly traded companies, building relationships with hedge funds, venture funds, family offices and institutional investors. He has held leadership roles on regional committees and museum boards, and holds a Bachelor of Arts in Biology.</p>
  </div>
  <div class="foot-logo">MCVF</div><div class="foot-line"></div><div class="foot-num">8</div>
</section>

<!-- Slide 9 : contact -->
<section class="slide" style="left:796px;top:503px">
  <div class="contact-h">CONTACT <em>US</em></div>
  <div class="contact-p">laoreet dolore magna aliquam erat volutpat. Ut wisi enim ad minim veniam, quis nostrud exerci.aliquam nostrud exerci.aliquam erat volutpat. Ut wisi enim.</div>
  <div class="contact-band">
    <div class="contact-item" style="left:20px">
      <svg width="9" height="9" viewBox="0 0 10 10"><circle cx="5" cy="5" r="4.6" fill="#fff"/><path d="M5 2.3a1.9 1.9 0 0 0-1.9 1.9C3.1 5.6 5 7.7 5 7.7s1.9-2.1 1.9-3.5A1.9 1.9 0 0 0 5 2.3z" fill="#1570c6"/><circle cx="5" cy="4.2" r=".7" fill="#fff"/></svg>
      <div>Address Street Name<br>City Name, Country 000</div>
    </div>
    <div class="contact-item" style="left:113px">
      <svg width="9" height="9" viewBox="0 0 10 10"><circle cx="5" cy="5" r="4.6" fill="#fff"/><path d="M3.3 2.8l1 .1.5 1.2-.6.5a4 4 0 0 0 1.3 1.3l.5-.6 1.2.5.1 1c-.3.4-.8.5-1.3.4A5 5 0 0 1 2.9 4c-.1-.5 0-1 .4-1.2z" fill="#1570c6"/></svg>
      <div>(+000) 123 456 789<br>(+000) 123 456 789</div>
    </div>
    <div class="contact-item" style="left:193px">
      <svg width="9" height="9" viewBox="0 0 10 10"><circle cx="5" cy="5" r="4.6" fill="#fff"/><rect x="2.6" y="3.4" width="4.8" height="3.2" rx=".4" fill="#1570c6"/><path d="M2.8 3.6L5 5.2l2.2-1.6" stroke="#fff" stroke-width=".5" fill="none"/></svg>
      <div>info@maplecrestfund.com<br>www.maplecrestfund.com</div>
    </div>
  </div>
  <div class="contact-web">www.<b>maplecrestfund</b>.com</div>
</section>

</body>
</html>
```